Lakeview Trailer Leasing

We need a website for our new Trailer leasing company.
Check out https://crestmoortrailerleasing.com/home for ideas.

Coding

Coded - Design and coding required

Number of Pages Required

4 page

```html
<!DOCTYPE html>
<html lang="en">
<head>
<meta charset="utf-8">
<title>Lakeview Trailer Leasing</title>
<link href="https://fonts.googleapis.com/css2?family=Titillium+Web:ital,wght@0,300;0,400;0,600;0,700;1,400;1,600;1,700&display=swap" rel="stylesheet">
<style>
:root{
  --blue:#0b4f8f;
  --blue-dark:#083d70;
  --cyan:#1ab3e3;
  --slate:#5c6b80;
  --ink:#1f2933;
  --text:#3b4450;
  --muted:#9aa3ad;
  --light:#edf0f8;
  --panel:#f3f5f6;
  --hero:#2f3c47;
  --footer:#1c232c;
  --white:#ffffff;
}
*{box-sizing:border-box;margin:0;padding:0}
html,body{width:1200px;height:4156px;overflow:hidden}
body{font-family:"Titillium Web",sans-serif;color:var(--text);background:var(--white)}
section,header,footer{position:relative;width:1200px;overflow:hidden}
.abs{position:absolute}
.btn{position:absolute;display:flex;align-items:center;justify-content:center;gap:8px;color:var(--white);font-weight:600;font-size:14px;border-radius:6px;background:var(--blue)}
.btn .arr{width:0;height:0;border-left:5px solid currentColor;border-top:4px solid transparent;border-bottom:4px solid transparent}
.ph{position:absolute;display:block}

/* header */
.site-header{height:92px;background:var(--white)}
.brand{position:absolute;left:173px;top:22px;display:flex;align-items:center;gap:10px}
.brand-mark{width:30px;height:30px;background:var(--blue)}
.brand-name{font-size:26px;font-weight:700;color:var(--blue);letter-spacing:.5px}
.auth{position:absolute;top:6px;display:flex;align-items:center;justify-content:center;height:30px;font-size:13px;font-weight:600;color:var(--white);border-radius:8px 8px 8px 0}
.auth.login{left:836px;width:95px;background:var(--slate)}
.auth.register{left:934px;width:94px;background:var(--blue)}
.main-nav{position:absolute;left:426px;top:58px;display:flex;font-size:14px;font-weight:600;color:var(--ink)}
.main-nav span{margin-right:34px}
.main-nav span:last-child{margin-right:0}

/* hero */
.hero{height:487px;background:var(--hero)}
.hero h1{position:absolute;left:178px;top:88px;width:410px;font-size:44px;line-height:53px;font-style:italic;font-weight:600;color:var(--white)}
.hero .btn-outline{position:absolute;left:169px;top:332px;width:118px;height:36px;border:2px solid var(--white);border-radius:6px;color:var(--white);font-size:14px;font-weight:600;display:flex;align-items:center;justify-content:center}
.dots{position:absolute;left:173px;top:427px;display:flex;gap:10px}
.dots i{display:block;width:47px;height:3px;background:rgba(255,255,255,.35)}
.dots i:first-child{background:var(--white)}

/* features */
.features{height:566px;background:var(--white)}
.connector{position:absolute;top:273px;height:3px}
.node{position:absolute;top:266px;width:17px;height:17px;border-radius:50%;background:var(--white);border:3px solid}
.feature{position:absolute;top:74px;width:236px;height:404px;border:4px solid;border-radius:24px;padding:12px}
.feature .inner{position:relative;width:100%;height:100%;background:var(--panel);border-radius:14px;box-shadow:0 6px 18px rgba(0,0,0,.08);text-align:center}
.feature .icon{position:absolute;left:50%;top:50px;width:90px;height:64px;margin-left:-45px;border-radius:10px}
.feature h3{position:absolute;left:0;right:0;top:128px;font-size:17px;font-weight:600;color:var(--ink)}
.feature p{position:absolute;left:14px;right:14px;top:163px;font-size:13px;line-height:23px;color:var(--text)}
.feature .btn{left:23px;top:318px;width:158px;height:36px;font-size:13px;border-radius:5px 5px 5px 0;box-shadow:0 6px 12px rgba(0,0,0,.15)}
.feature.blue{border-color:var(--blue)}
.feature.cyan{border-color:var(--cyan)}
.feature.slate{border-color:var(--slate)}
.dotted{position:absolute;border:3px dotted}

/* welcome */
.welcome{height:497px;background:var(--light)}
.welcome .kicker{position:absolute;left:173px;top:82px;font-size:40px;font-weight:300;color:var(--ink)}
.welcome .title{position:absolute;left:173px;top:128px;font-size:38px;font-weight:700;font-style:italic;color:var(--blue)}
.welcome p{position:absolute;left:173px;top:197px;width:415px;font-size:13.5px;line-height:24.6px}
.welcome .btn{left:173px;top:383px;width:118px;height:36px}
.welcome .ph{left:624px;top:99px;width:402px;height:330px;border-radius:8px;background:linear-gradient(120deg,#2c4a78 0%,#a83a34 40%,#c0413a 60%,#3b5583 100%)}

/* services */
.services{height:553px;background:linear-gradient(160deg,#3a4148 0%,#23292f 55%,#2c3338 100%)}
.service{position:absolute;top:90px;width:271px;height:371px;background:var(--white);border-radius:8px 8px 22px 8px;text-align:center}
.service .ph{left:15px;top:15px;width:241px;height:165px;border-radius:6px}
.service h3{position:absolute;left:0;right:0;top:203px;font-size:18px;font-weight:600;color:var(--ink);text-transform:uppercase}
.service p{position:absolute;left:12px;right:12px;top:231px;font-size:13.5px;line-height:19.5px}
.service .btn{left:43px;top:318px;width:186px;height:36px;font-size:13.5px}

/* about */
.about{height:495px;background:var(--white)}
.about .ph{left:173px;top:79px;width:330px;height:330px;border-radius:60px 12px 60px 12px}
.about h2{position:absolute;left:553px;top:110px;width:480px;font-size:36px;line-height:42px;font-weight:600;color:var(--ink)}
.about p{position:absolute;left:553px;top:213px;width:475px;font-size:13.5px;line-height:24.6px}
.about .btn{left:553px;top:329px;width:118px;height:35px}

/* blog */
.blog{height:568px;background:var(--light)}
.blog h2{position:absolute;left:0;right:0;top:36px;text-align:center;font-size:36px;font-weight:600;color:var(--ink)}
.post{position:absolute;top:107px;width:269px;height:374px;background:var(--white);border-radius:10px;box-shadow:0 4px 14px rgba(0,0,0,.06);overflow:hidden}
.post .ph{left:0;top:0;width:269px;height:177px}
.post .meta{position:absolute;left:21px;top:189px;font-size:12px;font-style:italic;color:var(--text)}
.post h3{position:absolute;left:21px;top:209px;font-size:18px;font-weight:600;color:var(--ink)}
.post p{position:absolute;left:21px;right:18px;top:242px;font-size:13.5px;line-height:21px}
.post .btn{left:21px;top:319px;width:117px;height:36px}

/* contact */
.contact{height:517px;background:var(--white)}
.contact .panel{position:absolute;left:173px;top:52px;width:345px;height:343px;background:var(--blue)}
.contact .panel .small{position:absolute;right:73px;top:139px;font-size:15px;font-weight:600;color:var(--white)}
.contact .panel .big{position:absolute;right:73px;top:160px;font-size:36px;font-weight:600;color:var(--white)}
.contact .frame{position:absolute;left:776px;top:46px;width:250px;height:248px;border:4px solid var(--blue)}
.form-card{position:absolute;left:473px;top:78px;width:535px;height:390px;background:var(--white);box-shadow:0 8px 30px rgba(0,0,0,.12)}
.form-card h2{position:absolute;left:32px;top:46px;font-size:34px;font-weight:600;color:var(--ink)}
.form-card h2 em{font-style:normal;color:var(--blue)}
.field{position:absolute}
.field label{display:block;font-size:14px;font-weight:600;color:var(--ink)}
.field .input{display:block;margin-top:6px;padding-bottom:4px;border-bottom:1px solid #b7bdc4;font-size:12.5px;color:var(--muted)}
.send{position:absolute;left:461px;top:307px;width:52px;height:52px;border-radius:50%;background:var(--blue);display:flex;align-items:center;justify-content:center}

/* footer */
.site-footer{height:381px;background:var(--footer);color:#d9dee4}
.site-footer .brand{left:173px;top:76px}
.site-footer .brand-mark{width:34px;height:34px;background:var(--white)}
.site-footer .brand-name{color:var(--white);font-size:28px}
.site-footer .about-text{position:absolute;left:173px;top:162px;width:270px;font-size:13.5px;line-height:22px}
.vline{position:absolute;top:48px;width:1px;height:250px;background:#3b4551}
.site-footer h4{position:absolute;top:60px;font-size:19px;font-weight:600;color:var(--white)}
.flink{position:absolute;font-size:13.5px}
.social{position:absolute;top:110px;left:887px;display:flex;gap:10px}
.social i{display:block;width:27px;height:27px;border-radius:50%;background:var(--white)}
.copy{position:absolute;left:0;right:0;top:338px;text-align:center;font-size:13.5px}
.copy span{color:var(--cyan)}
</style>
</head>
<body>

<header class="site-header">
  <div class="brand"><span class="brand-mark"></span><span class="brand-name">Lakeview</span></div>
  <div class="auth login">Login</div>
  <div class="auth register">Register</div>
  <nav class="main-nav">
    <span>Rent/Lease/Buy</span><span>Trailers</span><span>Services</span><span>Company</span><span>Careers</span><span>Blog</span><span>Contact Us</span>
  </nav>
</header>

<section class="hero">
  <svg class="abs" style="left:0;top:0" width="1200" height="487" role="img" aria-label="Photo of a white truck hauling a green shipping container on a highway">
    <defs>
      <linearGradient id="heroSky" x1="0" y1="0" x2="0" y2="1">
        <stop offset="0" stop-color="#4f7fb8"/>
        <stop offset=".45" stop-color="#9ab4cf"/>
        <stop offset=".55" stop-color="#6f7d86"/>
        <stop offset="1" stop-color="#3f474e"/>
      </linearGradient>
    </defs>
    <path d="M760 0 L1200 0 L1200 487 L562 487 C540 330 610 120 760 0 Z" fill="url(#heroSky)"/>
  </svg>
  <h1>Short-term trailer rentals, long-term leases and everything in between</h1>
  <div class="btn-outline">Know More</div>
  <div class="dots"><i></i><i></i><i></i></div>
</section>

<section class="features">
  <div class="dotted" style="left:174px;top:130px;width:120px;height:360px;border-color:var(--blue);border-right:none;border-top:none;border-radius:0 0 0 30px"></div>
  <div class="dotted" style="left:480px;top:70px;width:240px;height:200px;border-color:var(--cyan);border-bottom:none;border-radius:24px 24px 0 0"></div>
  <div class="dotted" style="left:900px;top:150px;width:126px;height:330px;border-color:var(--slate);border-left:none;border-top:none;border-radius:0 0 30px 0"></div>

  <div class="connector" style="left:411px;width:71px;background:var(--blue)"></div>
  <div class="connector" style="left:716px;width:71px;background:var(--cyan)"></div>
  <div class="node" style="left:403px;border-color:var(--blue)"></div>
  <div class="node" style="left:474px;border-color:var(--cyan)"></div>
  <div class="node" style="left:708px;border-color:var(--cyan)"></div>
  <div class="node" style="left:779px;border-color:var(--slate)"></div>

  <div class="feature blue" style="left:177px">
    <div class="inner">
      <span class="icon ph" style="background:linear-gradient(90deg,#f5b323 60%,#e2463b 60%)" role="img" aria-label="Illustration of a delivery truck"></span>
      <h3>Nationwide Coverage</h3>
      <p>Lorem ipsum dolor sit amet, consectetur adipiscing elit. Quisque us, imperdiet magna velconvallis metus. Nulla luctus eros ante, sed efficitur leo bibendum eget</p>
      <div class="btn">Find Locations <span class="arr"></span></div>
    </div>
  </div>
  <div class="feature cyan" style="left:482px">
    <div class="inner">
      <span class="icon ph" style="background:radial-gradient(circle,#f8c133 35%,#2aa6dc 80%)" role="img" aria-label="Illustration of a light bulb with gears"></span>
      <h3>Advanced Technology</h3>
      <p>Nulla egestas elit ante, at ultes ipsu dit. Suspaccumsan orre. Praesent sed convallis est. Fusce diam, tincidunt id hendr sed tincidunt. Nullam blandit magna</p>
      <div class="btn" style="background:var(--cyan)">Online Services <span class="arr"></span></div>
    </div>
  </div>
  <div class="feature slate" style="left:787px">
    <div class="inner">
      <span class="icon ph" style="background:radial-gradient(circle,#3c4a5a 40%,#f2a23a 75%)" role="img" aria-label="Illustration of interlocking gears"></span>
      <h3>Flexible Service</h3>
      <p>Nulla egestas elit ante, at ultes ipsu dit. Suspaccumsan orre. Praesent sed convallis est. Fusce diam, tincidunt id hendr sed tincidunt. Nullam blandit magna</p>
      <div class="btn" style="background:var(--slate)">Learn More About Us <span class="arr"></span></div>
    </div>
  </div>
</section>

<section class="welcome">
  <div class="kicker">Welcome to</div>
  <div class="title">Lakeview Trailer Leasing</div>
  <p>Lorem ipsum dolor sit amet, consectetur adipiscing elit. Quisque a libero cursus, imperdiet magna vel, convallis metus. Nulla luctus eros ante, sed efficitur leo bibendum eget. Mais et tempor nibh. Maecenas eu enim ullamcorper, lacinia felis nec, fringa ligula. Donec ter feugiat dolor eu laoreet. Aenean in condimentum sapien. Fusce non ultrices nunc, nec aliquet mauris. Ut in ante mimus, pharetra lectus vitae, bibendum lorem.</p>
  <div class="btn">Read More</div>
  <span class="ph" role="img" aria-label="Photo of a red container truck framed by a decorative blue curved shape"></span>
</section>

<section class="services">
  <div class="service" style="left:171px">
    <span class="ph" style="background:linear-gradient(135deg,#e6e8ea,#b9bec3)" role="img" aria-label="Photo of hands holding a tablet at a desk"></span>
    <h3>Credit Application</h3>
    <p>Lorem ipsum dolor sit amet, consectetur adipiscing elit. Quisque a libero cursus, imperdiet magna vel, convallis metus. Nulla luctus eros ante, sed</p>
    <div class="btn">Apply Online <span class="arr"></span></div>
  </div>
  <div class="service" style="left:465px">
    <span class="ph" style="background:linear-gradient(135deg,#56606b,#9aa5ae)" role="img" aria-label="Photo of a driver standing beside a car carrier truck"></span>
    <h3>Registrations / FHWA</h3>
    <p>Lorem ipsum dolor sit amet, consectetur adipiscing elit. Quisque a libero cursus, imperdiet magna vel, convallis metus. Nulla luctus eros ante, sed</p>
    <div class="btn">Find Registration <span class="arr"></span></div>
  </div>
  <div class="service" style="left:757px">
    <span class="ph" style="background:linear-gradient(135deg,#a7b86a,#e7d3b8)" role="img" aria-label="Photo of a woman on a phone call outdoors"></span>
    <h3>Request A Quote</h3>
    <p>Lorem ipsum dolor sit amet, consectetur adipiscing elit. Quisque a libero cursus, imperdiet magna vel, convallis metus. Nulla luctus eros ante, sed</p>
    <div class="btn">Get A Quote <span class="arr"></span></div>
  </div>
</section>

<section class="about">
  <span class="ph" style="background:linear-gradient(180deg,#aac3d8 0%,#c9d2d9 45%,#8a949c 100%)" role="img" aria-label="Photo of hands holding a tablet in front of a row of trucks"></span>
  <h2>Etiam sodales arcu vel diam venenatis at laoreet tellus</h2>
  <p>Pellentesque vel rhoncus diam. Vivamus elementum rutrci vnatis pellentesque. Proin pellentesque erat quis turpis varius aliquam. Integer volutpat leo egestas orci iaculis, et rutrum magna sollicitudin. Proin eget tuus. Praesent sollicitudin, ex sed vulputate eleifend, diam turpis elementum diam.</p>
  <div class="btn">Read More</div>
</section>

<section class="blog">
  <h2>Latest Blog</h2>
  <div class="post" style="left:171px">
    <span class="ph" style="background:linear-gradient(180deg,#7fa9d6,#d4d8dc 60%,#8d9296)" role="img" aria-label="Photo of a driver walking beside a white trailer"></span>
    <div class="meta">Feb 20, 2022 &nbsp;&nbsp;| &nbsp;&nbsp;Posted by John Doe</div>
    <h3>Suspendisse accumsan</h3>
    <p>Proin eget tuus. Praesent sollicitudin, ex sed vulputate eleifend, diam turpis elementum diam.</p>
    <div class="btn">Read More</div>
  </div>
  <div class="post" style="left:463px">
    <span class="ph" style="background:linear-gradient(180deg,#e9a15a,#c0283a 55%,#3a3f48)" role="img" aria-label="Photo of a red semi truck on a road at sunset"></span>
    <div class="meta">Feb 20, 2022 &nbsp;&nbsp;| &nbsp;&nbsp;Posted by John Doe</div>
    <h3>Suspendisse accumsan</h3>
    <p>Proin eget tuus. Praesent sollicitudin, ex sed vulputate eleifend, diam turpis elementum diam.</p>
    <div class="btn">Read More</div>
  </div>
  <div class="post" style="left:755px">
    <span class="ph" style="background:linear-gradient(180deg,#c9d6e2,#8b8f92 60%,#5c6065)" role="img" aria-label="Photo of a grey trailer truck on a highway"></span>
    <div class="meta">Feb 20, 2022 &nbsp;&nbsp;| &nbsp;&nbsp;Posted by John Doe</div>
    <h3>Suspendisse accumsan</h3>
    <p>Proin eget tuus. Praesent sollicitudin, ex sed vulputate eleifend, diam turpis elementum diam.</p>
    <div class="btn">Read More</div>
  </div>
</section>

<section class="contact">
  <div class="panel">
    <div class="small">Contact Us</div>
    <div class="big">Get In Touch</div>
  </div>
  <div class="frame"></div>
  <div class="form-card">
    <h2>Send Us <em>Message</em></h2>
    <div class="field" style="left:32px;top:112px;width:225px"><label>Your Name</label><span class="input">Enter your name</span></div>
    <div class="field" style="left:279px;top:112px;width:223px"><label>Email Address</label><span class="input">Enter email</span></div>
    <div class="field" style="left:32px;top:170px;width:225px"><label>Phone</label><span class="input" style="margin-top:12px">Enter Phone no</span></div>
    <div class="field" style="left:279px;top:170px;width:223px"><label>Subject</label><span class="input" style="margin-top:12px">Your Subject</span></div>
    <div class="field" style="left:32px;top:235px;width:420px"><label>Message</label><span class="input" style="margin-top:20px;padding-bottom:12px">Type your message</span></div>
    <div class="send">
      <svg width="24" height="24" viewBox="0 0 24 24" aria-hidden="true"><path d="M2 11 L22 2 L15 22 L11 13 Z" fill="#fff"/><path d="M11 13 L22 2" stroke="#0b4f8f" stroke-width="1.5"/></svg>
    </div>
  </div>
</section>

<footer class="site-footer">
  <div class="brand"><span class="brand-mark"></span><span class="brand-name">Lakeview</span></div>
  <p class="about-text">Lorem ipsum dolor sit amet, consectetur adipiscing elit, sed do eiusmod ter incididunt ut labore et dolore magna aliqua. Quis ipsum suspendisse ultrices graa. Risu comodo viverra maecenas accus vel facilisis.</p>
  <div class="vline" style="left:503px"></div>
  <div class="vline" style="left:826px"></div>
  <h4 style="left:578px">Quick Links</h4>
  <span class="flink" style="left:578px;top:110px">Rent/Lease/Buy</span>
  <span class="flink" style="left:578px;top:150px">Trailers</span>
  <span class="flink" style="left:578px;top:190px">Services</span>
  <span class="flink" style="left:578px;top:231px">Company</span>
  <span class="flink" style="left:702px;top:110px">Careers</span>
  <span class="flink" style="left:702px;top:150px">Blog</span>
  <span class="flink" style="left:702px;top:190px">Contact Us</span>
  <h4 style="left:887px">Follow Us</h4>
  <div class="social"><i></i><i></i><i></i><i></i></div>
  <div class="copy">© 2022 <span>Lakeview Trailer Leasing</span>. All right reserved</div>
</footer>

</body>
</html>
```